Ovalin Designs LTD

Van Wrap
Halvorn Quesk 2010 Red
Media Walls
False Ceiling Design
Fretwork Designs

Target Market(s)

Everyone

Industry/Entity Type

Cinstruction I

Requirements
Must have
• Media Walls , Ceiling Designs, Logo, Logo with Motto
Nice to have
• I want the images to 3d and paint everything about my work with less words

```html
<!DOCTYPE html>
<html lang="en">
<head>
<meta charset="utf-8">
<title>Ovalin Designs LTD – Van Wrap</title>
<link rel="stylesheet" href="https://fonts.googleapis.com/css2?family=Montserrat:wght@600;700&display=swap">
<style>
  :root {
    --page: #e9e9e9;
    --van-white: #f7f7f7;
    --brand-blue: #0f2f8f;
    --brand-orange: #ef9a4b;
    --trim: #2a2a2a;
    --glass: #3c4148;
    --tyre: #1e1e1e;
    --hub: #b9bcc0;
    --text-light: #ffffff;
  }
  html, body {
    margin: 0;
    padding: 0;
    width: 1200px;
    height: 1200px;
    overflow: hidden;
    background: var(--page);
  }
  .wrap-canvas {
    display: block;
    width: 1200px;
    height: 1200px;
  }
  .brand-name {
    font-family: "Montserrat", sans-serif;
    font-weight: 700;
    font-size: 15px;
    fill: var(--brand-blue);
    letter-spacing: 0.5px;
  }
  .service-list {
    font-family: "Montserrat", sans-serif;
    font-weight: 600;
    font-size: 14px;
    fill: var(--text-light);
  }
  .phone-number {
    font-family: "Montserrat", sans-serif;
    font-weight: 700;
    font-size: 17px;
    fill: var(--text-light);
  }
</style>
</head>
<body>
<svg class="wrap-canvas" viewBox="0 120 960 720" xmlns="http://www.w3.org/2000/svg" aria-label="Ovalin Designs LTD van wrap, side view">
  <defs>
    <clipPath id="van-body-clip">
      <path d="M72,602 L76,552 Q80,500 100,480 L215,420 Q265,360 320,342 Q340,335 380,335 L875,333 Q898,340 902,370 L906,588 Q906,600 895,600 L72,602 Z"/>
    </clipPath>
    <linearGradient id="wrap-band-gradient" x1="0" y1="0" x2="1" y2="0">
      <stop offset="0" stop-color="var(--brand-orange)"/>
      <stop offset="0.35" stop-color="var(--brand-blue)"/>
      <stop offset="1" stop-color="var(--brand-blue)"/>
    </linearGradient>
    <linearGradient id="wrap-rear-gradient" x1="0" y1="0" x2="0" y2="1">
      <stop offset="0" stop-color="var(--brand-blue)"/>
      <stop offset="1" stop-color="#1a3aa0"/>
    </linearGradient>
  </defs>

  <!-- van body -->
  <g class="van-body">
    <path fill="var(--van-white)" d="M72,602 L76,552 Q80,500 100,480 L215,420 Q265,360 320,342 Q340,335 380,335 L875,333 Q898,340 902,370 L906,588 Q906,600 895,600 L72,602 Z"/>

    <g class="wrap-graphics" clip-path="url(#van-body-clip)" role="img" aria-label="Decorative blue and orange wave pattern of the wrap">
      <rect class="wrap-rear-area" x="640" y="325" width="275" height="290" fill="url(#wrap-rear-gradient)"/>
      <rect class="wrap-lower-band" x="262" y="495" width="653" height="120" fill="url(#wrap-band-gradient)"/>
      <rect class="bumper" x="60" y="575" width="60" height="40" fill="var(--trim)"/>
      <rect class="rear-bumper" x="860" y="540" width="50" height="70" fill="var(--trim)" opacity="0.85"/>
    </g>

    <!-- windows and trim -->
    <path class="side-window" fill="var(--glass)" d="M300,380 Q320,355 345,352 L440,350 L440,452 L290,455 L282,430 Z"/>
    <path class="quarter-window" fill="var(--glass)" d="M225,460 L280,395 L283,455 Z"/>
    <line class="door-seam" x1="462" y1="342" x2="462" y2="600" stroke="var(--trim)" stroke-opacity="0.25" stroke-width="1.5"/>
    <line class="door-seam" x1="272" y1="440" x2="272" y2="600" stroke="var(--trim)" stroke-opacity="0.25" stroke-width="1.5"/>
    <rect class="rub-strip" x="288" y="558" width="612" height="9" rx="3" fill="var(--trim)" opacity="0.9"/>
    <rect class="door-handle" x="406" y="471" width="50" height="9" rx="4" fill="var(--trim)"/>
    <rect class="tail-light" x="886" y="368" width="15" height="80" rx="4" fill="#c9241f"/>
  </g>

  <!-- wheels -->
  <g class="wheels">
    <circle cx="188" cy="598" r="64" fill="var(--page)"/>
    <circle cx="188" cy="598" r="58" fill="var(--tyre)"/>
    <circle cx="188" cy="598" r="36" fill="var(--hub)"/>
    <circle cx="188" cy="598" r="10" fill="#6e7276"/>
    <circle cx="742" cy="598" r="64" fill="var(--page)"/>
    <circle cx="742" cy="598" r="56" fill="var(--tyre)"/>
    <circle cx="742" cy="598" r="35" fill="var(--hub)"/>
    <circle cx="742" cy="598" r="10" fill="#6e7276"/>
  </g>

  <!-- brand -->
  <g class="brand-block">
    <rect x="480" y="362" width="44" height="44" fill="var(--brand-blue)"/>
    <text class="brand-name" x="534" y="381">OVALIN</text>
    <text class="brand-name" x="534" y="400">DESIGNS</text>
  </g>

  <!-- services -->
  <text class="service-list">
    <tspan x="665" y="383">Media Walls</tspan>
    <tspan x="665" y="402">False Ceiling Design</tspan>
    <tspan x="665" y="420">Fretwork Designs</tspan>
  </text>

  <!-- phone -->
  <g class="phone-line">
    <circle cx="493" cy="521" r="8" fill="none" stroke="var(--text-light)" stroke-width="1.8"/>
    <path d="M489.5,517 q-1,3 2,6.5 q3,2.5 5.5,2 l0.5,-2 l-2,-1.2 l-1.2,1 q-2,-1 -3,-3 l1,-1.2 l-1.2,-2 Z" fill="var(--text-light)"/>
    <text class="phone-number" x="509" y="527">1480-317-629</text>
  </g>
</svg>
</body>
</html>
```